Step repeat logo/Pull ups

Urgent Large Format Print Designer Needed — Today/Tomorrow

Hello, I need an experienced large-format print designer to redesign several event banners for my company, Tallowfen Insurance Agency Inc.

I created the initial concepts using ChatGPT, but the files are not high enough quality for printing. I do not need someone to simply upscale the images. I need someone who can rebuild the designs professionally from scratch so they are clean, sharp, print-ready, and accepted by PressMoor or any professional printer.

This project is urgent. I need someone who is available today and tomorrow because I need these files completed ASAP in order to print and receive them on time.

We are designing approximately 7 pieces, including:

1. Step-and-repeat backdrop — 10 ft × 8 ft
2. Pull-up banners — 47 in × 81 in
3. Welcome banner
4. Sponsor thank-you banner
5. Brand values banner
6. Brand essence banner
7. Motivation / AEP Kick-Off event banners

The style must match our brand: professional, premium, clean, modern, corporate, inspiring, and high-quality. Our colors are navy, blue, purple, white, and gold accents.

Important requirements:

* Use the official Tallowfen logo exactly as provided
* Do not recreate, redraw, distort, or modify the logo
* Text must be clean, readable, and print-sharp
* Final files must be built at the correct real print sizes
* Must include proper bleed and safe margins
* Must be print-ready for PressMoor or large-format printing
* Must provide editable source files
* Fonts must be outlined or included
* No blurry images
* No AI-looking letters
* No spelling mistakes
* No low-resolution graphics

Required final deliverables:

* Editable AI, EPS, or layered PDF source file
* Print-ready PDF
* High-resolution PNG
* JPG backup if possible
* All files sized correctly:
* Step backdrop: 10 ft × 8 ft
* Pull-ups: 47 in × 81 in

I already have the design direction, logo, colors, and examples. I need a designer who can take the concept and make it truly professional for print.

Please only apply if you have experience with large-format banners, step-and-repeat backdrops, pull-up banners, trade show graphics, and print production.

If you do not have time today or tomorrow, please do not apply.
If you do not know how to design at this level for professional printing, please do not apply.

Thank you.

Target Market(s)

Insurance Brokers Event/Motivational event

Colors
0054AA
0677BA
7BADD7
CADEEF
E8F1F8
0094D4
00A9DD
6FCCEA
C7EBF8
E9F6FB
6B429C
8869AF
B7A5CE
E3DAEB
F3F0F8

```html
<!DOCTYPE html>
<html lang="en">
<head>
<meta charset="utf-8">
<title>Tallowfen Pull-Up Banner</title>
<link href="https://fonts.googleapis.com/css2?family=Poppins:wght@500;600;700;800;900&family=Kaushan+Script&display=swap" rel="stylesheet">
<style>
  :root {
    --stage: #8a8a8a;
    --navy: #02133a;
    --deep-purple: #4e1566;
    --purple: #9c4dbb;
    --violet: #6b429c;
    --sky: #29b2f6;
    --cyan: #4dcbff;
    --blue: #0677ba;
    --ink: #0b2161;
    --white: #ffffff;
    --mist: #e3e6fb;
  }
  * { margin: 0; padding: 0; box-sizing: border-box; }
  html, body { width: 748px; height: 1200px; overflow: hidden; }
  body {
    background: var(--stage);
    font-family: "Poppins", sans-serif;
    position: relative;
  }
  .stage-label {
    position: absolute; left: 0; width: 748px; text-align: center;
    color: var(--white); font-weight: 800; font-size: 25px; letter-spacing: 0.5px;
  }
  .stage-label--top { top: 28px; }
  .stage-label--size { top: 1120px; }

  .banner {
    position: absolute; left: 75px; top: 76px; width: 601px; height: 1035px;
    overflow: hidden;
  }
  .banner__art { position: absolute; inset: 0; }

  .brand {
    position: absolute; left: 0; top: 0; width: 601px; height: 190px;
  }
  .brand__name {
    position: absolute; left: 0; top: 44px; width: 601px;
    display: flex; justify-content: center; align-items: center; gap: 10px;
    font-weight: 600; font-size: 62px; line-height: 1; color: var(--deep-purple);
    letter-spacing: -1px;
  }
  .brand__dot {
    width: 22px; height: 22px; border-radius: 50%; background: var(--blue);
  }
  .brand__sub {
    position: absolute; right: 63px; top: 112px;
    font-weight: 500; font-size: 26px; color: var(--sky); line-height: 1;
  }
  .brand__partner {
    position: absolute; left: 0; width: 601px; top: 157px;
    display: flex; justify-content: center; align-items: center; gap: 8px;
    font-weight: 600; font-size: 13.5px; letter-spacing: 2.6px; color: #3a3a4a;
    line-height: 1;
  }
  .brand__partner::before, .brand__partner::after {
    content: ""; width: 40px; height: 1px; background: #3a3a4a;
  }

  .pillars { position: absolute; left: 0; width: 601px; top: 288px; text-align: center; }
  .pillar { line-height: 0.92; font-weight: 900; text-transform: uppercase; }
  .pillar__lead { display: block; color: var(--white); font-size: 58px; letter-spacing: -0.5px; }
  .pillar__key { display: block; font-size: 68px; letter-spacing: -0.5px; }
  .pillar__key--sky { color: var(--sky); }
  .pillar__key--purple { color: var(--purple); }
  .pillar__key--cyan { color: var(--cyan); }
  .pillar-rule {
    width: 310px; height: 2px; margin: 20px auto 16px;
    background: radial-gradient(ellipse at center, #6fd2ff 0%, #1a5cff 35%, rgba(10,40,160,0) 75%);
  }

  .offers {
    position: absolute; left: 0; top: 744px; width: 601px; height: 72px;
  }
  .offer {
    position: absolute; top: 0; width: 120px; margin-left: -60px; text-align: center;
    color: var(--white); font-size: 16.5px; font-weight: 500;
  }
  .offer svg { display: block; margin: 0 auto 10px; }
  .offer-divider {
    position: absolute; top: 2px; width: 1px; height: 70px; background: #2a6fd0;
  }

  .closing { position: absolute; left: 0; width: 601px; top: 923px; text-align: center; }
  .closing__line { font-weight: 600; font-size: 17px; color: var(--ink); }
  .closing__script {
    font-family: "Kaushan Script", cursive; font-size: 46px; color: var(--sky);
    line-height: 1.1; margin-top: 2px;
  }
  .closing__swoosh { display: block; margin: -6px auto 0; }
</style>
</head>
<body>
  <div class="stage-label stage-label--top">PULL-UP BANNER</div>

  <section class="banner">
    <svg class="banner__art" viewBox="0 0 601 1035" width="601" height="1035">
      <defs>
        <linearGradient id="paper" x1="0" y1="0" x2="1" y2="0">
          <stop offset="0" stop-color="#e4e7fb"/>
          <stop offset="0.5" stop-color="#ffffff"/>
          <stop offset="1" stop-color="#dfe3fb"/>
        </linearGradient>
        <linearGradient id="topPurple" x1="0" y1="0" x2="1" y2="0">
          <stop offset="0" stop-color="#4e1566"/>
          <stop offset="0.45" stop-color="#8a64e0"/>
          <stop offset="0.6" stop-color="#5a1b78"/>
          <stop offset="1" stop-color="#5a1b78"/>
        </linearGradient>
        <linearGradient id="topBlue" x1="0" y1="0" x2="1" y2="0">
          <stop offset="0" stop-color="#1fa7f2"/>
          <stop offset="0.6" stop-color="#24b1fa"/>
          <stop offset="1" stop-color="#0b63c4"/>
        </linearGradient>
        <linearGradient id="bottomPurple" x1="0" y1="0" x2="1" y2="0">
          <stop offset="0" stop-color="#8b45c0"/>
          <stop offset="1" stop-color="#4a1470"/>
        </linearGradient>
        <linearGradient id="bottomBlue" x1="0" y1="0" x2="1" y2="0">
          <stop offset="0" stop-color="#0a4fb0"/>
          <stop offset="1" stop-color="#2ab8f6"/>
        </linearGradient>
        <radialGradient id="glowLeft" cx="0" cy="0.2" r="0.35">
          <stop offset="0" stop-color="#1d5a8a" stop-opacity="0.8"/>
          <stop offset="1" stop-color="#02133a" stop-opacity="0"/>
        </radialGradient>
        <radialGradient id="glowRight" cx="1" cy="0.72" r="0.3">
          <stop offset="0" stop-color="#1d6a92" stop-opacity="0.8"/>
          <stop offset="1" stop-color="#02133a" stop-opacity="0"/>
        </radialGradient>
      </defs>
      <rect width="601" height="1035" fill="url(#paper)"/>
      <path d="M0 175 Q330 320 601 195 L601 1000 L0 1000 Z" fill="#02133a"/>
      <path d="M0 175 Q330 320 601 195 L601 1000 L0 1000 Z" fill="url(#glowLeft)"/>
      <path d="M0 175 Q330 320 601 195 L601 1000 L0 1000 Z" fill="url(#glowRight)"/>
      <path d="M0 132 Q330 290 601 162 L601 176 Q330 300 0 170 Z" fill="url(#topPurple)"/>
      <path d="M0 170 Q330 300 601 176 L601 196 Q330 322 0 176 Z" fill="url(#topBlue)"/>
      <path d="M0 835 Q140 905 300 880 Q140 915 0 935 Z" fill="url(#bottomBlue)"/>
      <path d="M0 1000 Q300 780 601 920 L601 960 Q300 830 0 990 Z" fill="url(#bottomPurple)"/>
      <path d="M0 990 Q300 830 601 960 L601 1035 L0 1035 Z" fill="url(#paper)"/>
    </svg>

    <header class="brand">
      <div class="brand__name"><span>Tallowfen</span><span class="brand__dot"></span></div>
      <div class="brand__sub">Insurance Agency</div>
      <div class="brand__partner">AN ALDERVALE PARTNER OFFICE</div>
    </header>

    <div class="pillars">
      <h2 class="pillar"><span class="pillar__lead">Build with</span><span class="pillar__key pillar__key--sky">Integrity.</span></h2>
      <div class="pillar-rule"></div>
      <h2 class="pillar"><span class="pillar__lead">Serve with</span><span class="pillar__key pillar__key--purple">Purpose.</span></h2>
      <div class="pillar-rule"></div>
      <h2 class="pillar"><span class="pillar__lead">Grow</span><span class="pillar__key pillar__key--cyan">Together.</span></h2>
    </div>

    <div class="offers">
      <div class="offer" style="left:91px">
        <svg width="46" height="46" viewBox="0 0 46 46" fill="none" stroke="#29b2f6" stroke-width="2.4">
          <circle cx="23" cy="23" r="16" stroke-width="7" stroke-dasharray="6 6.6"/>
          <circle cx="23" cy="23" r="13.5"/>
          <circle cx="23" cy="23" r="7"/>
        </svg>
        TOOLS
      </div>
      <div class="offer-divider" style="left:155px"></div>
      <div class="offer" style="left:233px">
        <svg width="56" height="46" viewBox="0 0 56 46" fill="none" stroke="#9c4dbb" stroke-width="2.4" stroke-linejoin="round">
          <path d="M28 10 Q18 3 6 5 L6 36 Q18 34 28 41 Q38 34 50 36 L50 5 Q38 3 28 10 Z"/>
          <path d="M28 10 L28 41"/>
          <path d="M2 10 L2 42 L54 42 L54 10"/>
        </svg>
        TRAINING
      </div>
      <div class="offer-divider" style="left:308px"></div>
      <div class="offer" style="left:373px">
        <svg width="64" height="46" viewBox="0 0 64 46" fill="none" stroke="#29b2f6" stroke-width="2.4">
          <circle cx="14" cy="12" r="6"/><circle cx="50" cy="12" r="6"/><circle cx="32" cy="10" r="8"/>
          <path d="M4 38 Q4 24 14 24 Q18 24 20 26"/>
          <path d="M60 38 Q60 24 50 24 Q46 24 44 26"/>
          <path d="M18 44 Q18 24 32 24 Q46 24 46 44 Z"/>
        </svg>
        SUPPORT
      </div>
      <div class="offer-divider" style="left:447px"></div>
      <div class="offer" style="left:514px">
        <svg width="50" height="46" viewBox="0 0 50 46" fill="none" stroke="#9c4dbb" stroke-width="2.4">
          <rect x="4" y="28" width="9" height="16"/><rect x="18" y="22" width="9" height="22"/><rect x="32" y="14" width="9" height="30"/>
          <path d="M2 44 L48 44"/>
          <path d="M2 18 Q24 12 45 2"/><path d="M38 2 L45 2 L44 9"/>
        </svg>
        GROWTH
      </div>
    </div>

    <footer class="closing">
      <p class="closing__line">Building Brokers. Service Communities</p>
      <p class="closing__script">This Is Personal</p>
      <svg class="closing__swoosh" width="200" height="8" viewBox="0 0 200 8">
        <path d="M2 6 Q100 0 198 2 Q100 3 2 6 Z" fill="#1d8fe0" stroke="#1d8fe0" stroke-width="2"/>
      </svg>
    </footer>
  </section>

  <div class="stage-label stage-label--size">47 IN × 81 IN</div>
</body>
</html>
```